Pelvane Tonic Social Media Graphics

Focusing on the Pelvane Tonic product, create 6-7 individual social media graphics (square size). For the color scheme of the graphics, they should all be complementary with the Pelvane Tonic bottle colors.

Note: each graphic should have one of the 3 pictures of the bottle on it and/or one of the images with a person on it (several pics attached)/only use stock photography that I provided.

Target Market(s)

men and women who need to lose weight

Industry/Entity Type

health and wellness

Colors
A7469A
B969AE
D3A5CF
EDDBEB
F8F0F9

Requirements
Must have
• product pictures
Nice to have
• stock photography that is included

```html
<!DOCTYPE html>
<html lang="en">
<head>
<meta charset="utf-8">
<title>Pelvane Tonic Social Media Graphics</title>
<link rel="stylesheet" href="https://fonts.googleapis.com/css2?family=Figtree:wght@600;700;800&display=swap">
<style>
  :root {
    --board: #000000;
    --blush: #eeb5d4;
    --plum: #5a1f5c;
    --plum-text: #5e2462;
    --ink: #000000;
    --photo-plum: #7a3c72;
    --photo-skin: #9a6a5a;
    --bottle: #f4eef3;
    --bottle-edge: #d9bfd6;
  }
  html, body {
    margin: 0;
    width: 1200px;
    height: 927px;
    overflow: hidden;
    background: var(--board);
  }
  .board {
    display: block;
    width: 1200px;
    height: 927px;
    font-family: "Figtree", sans-serif;
  }
  .tile-bg { fill: var(--blush); }
  .band { fill: var(--board); }
  .panel { fill: var(--plum); }
  .photo { fill: url(#photoTone); }
  .bottle { fill: var(--bottle); stroke: var(--bottle-edge); stroke-width: 3; }
  .headline { font-weight: 800; font-size: 62px; fill: var(--ink); }
  .headline .accent { fill: var(--plum-text); }
  .accent-line { fill: var(--plum-text); }
  .subline { font-weight: 700; font-size: 40px; fill: var(--ink); }
  .lead { font-weight: 700; font-size: 44px; fill: var(--ink); }
</style>
</head>
<body>
<svg class="board" viewBox="0 0 2184 1686" xmlns="http://www.w3.org/2000/svg">
  <defs>
    <linearGradient id="photoTone" x1="0" y1="0" x2="0" y2="1">
      <stop offset="0" stop-color="#8a5a6a"/>
      <stop offset="1" stop-color="#6a2e62"/>
    </linearGradient>
  </defs>
  <rect width="2184" height="1686" fill="var(--board)"/>

  <!-- Tile 1: Accelerate -->
  <g class="tile tile-accelerate">
    <rect class="tile-bg" x="114" y="235" width="588" height="585"/>
    <path class="band" d="M702,293 L380,560 Q320,610 320,680 L320,820 L702,820 Z"/>
    <path class="panel" d="M702,340 L400,590 Q358,625 358,680 L358,820 L702,820 Z"/>
    <rect class="photo" x="480" y="470" width="222" height="350" rx="20" role="img" aria-label="Smiling woman in sportswear holding an apple and a bathroom scale"/>
    <rect class="bottle" x="126" y="655" width="170" height="112" rx="14" role="img" aria-label="Three Pelvane Tonic bottles"/>
    <text class="lead" x="146">
      <tspan x="146" y="313">Accelerate Your</tspan>
      <tspan x="146" y="377">Weight Loss</tspan>
      <tspan x="146" y="441">With This</tspan>
      <tspan x="146" y="505">Easy Fat</tspan>
      <tspan x="146" y="569">Flush</tspan>
    </text>
  </g>

  <!-- Tile 2: Struggling -->
  <g class="tile tile-struggling">
    <rect class="tile-bg" x="786" y="235" width="588" height="585"/>
    <path class="band" d="M786,293 L1106,560 Q1166,610 1166,680 L1166,820 L786,820 Z"/>
    <path class="panel" d="M786,340 L1080,590 Q1130,625 1130,680 L1130,820 L786,820 Z"/>
    <rect class="photo" x="790" y="535" width="295" height="285" rx="20" role="img" aria-label="Cheerful woman flexing and holding a bathroom scale"/>
    <rect class="bottle" x="1236" y="635" width="84" height="150" rx="14" role="img" aria-label="Pelvane Tonic bottle"/>
    <text class="headline accent-line" x="1368" y="312" text-anchor="end">STRUGGLING TO</text>
    <text class="headline" x="1368" y="372" text-anchor="end">LOSE WEIGHT?</text>
    <text class="subline" text-anchor="middle">
      <tspan x="1174" y="455">Try This Fat Flush</tspan>
      <tspan x="1132" y="513">Secret</tspan>
    </text>
  </g>

  <!-- Tile 3: Burn fat faster -->
  <g class="tile tile-burn">
    <rect class="tile-bg" x="1464" y="235" width="604" height="595"/>
    <path class="band" d="M1464,775 L1735,555 Q1762,533 1789,555 L2068,790 L2068,830 L1464,830 Z"/>
    <path class="panel" d="M1490,830 L1762,590 L2056,830 Z"/>
    <rect class="photo" x="1610" y="585" width="290" height="245" role="img" aria-label="Woman measuring her waist with a tape measure"/>
    <rect class="bottle" x="1948" y="478" width="97" height="167" rx="14" role="img" aria-label="Pelvane Tonic bottle"/>
    <text class="headline" x="1766" y="312" text-anchor="middle"><tspan class="accent">BURN FAT</tspan> FASTER</text>
    <text class="subline" text-anchor="middle">
      <tspan x="1766" y="372">Discover the Simple Detox</tspan>
      <tspan x="1766" y="430">Your Body Needs!</tspan>
    </text>
  </g>

  <!-- Tile 4: Cleanse -->
  <g class="tile tile-cleanse">
    <rect class="tile-bg" x="114" y="878" width="588" height="586"/>
    <path class="band" d="M114,940 L430,1200 Q495,1255 495,1330 L495,1464 L114,1464 Z"/>
    <path class="panel" d="M114,985 L400,1230 Q458,1280 458,1340 L458,1464 L114,1464 Z"/>
    <rect class="photo" x="114" y="1030" width="341" height="434" role="img" aria-label="Slim waist wrapped in a tape measure"/>
    <rect class="bottle" x="555" y="1282" width="88" height="155" rx="14" role="img" aria-label="Pelvane Tonic bottle"/>
    <text class="headline accent-line" x="670" y="952" text-anchor="end">CLEANSE YOUR</text>
    <text class="headline" x="672" text-anchor="end">
      <tspan x="672" y="1024">LIVER, BURN</tspan>
      <tspan x="672" y="1096">FAT FASTER</tspan>
    </text>
    <text class="subline" text-anchor="end">
      <tspan x="684" y="1185">The Ultimate</tspan>
      <tspan x="684" y="1242">Solution</tspan>
    </text>
  </g>

  <!-- Tile 5: Hidden key -->
  <g class="tile tile-hidden">
    <rect class="tile-bg" x="786" y="878" width="588" height="586"/>
    <path class="band" d="M1374,935 L1055,1190 Q995,1240 995,1320 L995,1464 L1374,1464 Z"/>
    <path class="panel" d="M1374,985 L1080,1225 Q1030,1265 1030,1330 L1030,1464 L1374,1464 Z"/>
    <rect class="photo" x="1075" y="1175" width="299" height="289" rx="20" role="img" aria-label="Cheerful woman flexing and holding a bathroom scale"/>
    <rect class="bottle" x="838" y="1278" width="87" height="150" rx="14" role="img" aria-label="Pelvane Tonic bottle"/>
    <text class="headline accent-line" x="800" y="955">THE HIDDEN</text>
    <text class="headline">
      <tspan x="800" y="1015">KEY TO WEIGHT</tspan>
      <tspan x="800" y="1075">LOSS</tspan>
    </text>
    <text class="lead" x="800" y="1142">Liver Health</text>
  </g>

  <!-- Tile 6: Detox -->
  <g class="tile tile-detox">
    <rect class="tile-bg" x="1464" y="878" width="604" height="594"/>
    <path class="band" d="M1464,1418 L1735,1198 Q1762,1176 1789,1198 L2068,1433 L2068,1472 L1464,1472 Z"/>
    <path class="panel" d="M1490,1472 L1762,1228 L2056,1472 Z"/>
    <rect class="photo" x="1575" y="1228" width="330" height="244" role="img" aria-label="Toned woman in white sportswear with hands on hips"/>
    <rect class="bottle" x="1885" y="1163" width="170" height="115" rx="14" role="img" aria-label="Three Pelvane Tonic bottles"/>
    <text class="headline" x="1766" y="955" text-anchor="middle"><tspan class="accent">DETOX AND</tspan> BURN</text>
    <text class="headline" x="1766" y="1015" text-anchor="middle">FAT</text>
    <text class="subline" text-anchor="middle">
      <tspan x="1764" y="1080">The 1-Step Solution for</tspan>
      <tspan x="1750" y="1138">a Slimmer You</tspan>
    </text>
  </g>
</svg>
</body>
</html>
```